Logo and metal business card design

Updated added my current logo which focus needs to be concentrated on. Have to have the new logo before the card. Company name is The Calder Works, LLC

Update: Reminder this is a Logo and business card design. I want the logo to be “CalderW” in a unique professional design that says secure, insurance, financial.

The G needs to be a P in the cut out

Update: the top two images have design on the metal which I am looking for

New black metal business cards. And CalderW.com logo that will go on the card. This will be a cut out design in the metal. Featuring “CalderW.com as the main cutout. Like the idea of .com to be separate or smaller and possible color. Looking for unique CalderW font design and a surrounding design per the examples below. Calder and G need to be different and the G a specific designing the mesh like the attached with the V in the mesh. But card side ways.. so mesh on right side of card with a G and .com in lower corner or where it fits Also looking to add my main info on the back side of the card. Derek M. Cell Email@mailbox-example.net We are an commercial insurance broker specializing in program business.
Updates

Need more time not enough entry’s and they are all the same.. I’m suppose to get 75 plus and not 20 that are the exact same from artist??? Need more submissions to compare. I committed my money so I do not want a refund I want more submissions from different artist

Target Market(s)

Insurance for the Restaurant industry

Industry/Entity Type

Insurance Broker

Contact Information for Business Card

New black metal business cards. And CalderW.com logo that will go on the card. This will be a cut out design in the metal. Featuring “CalderW.com as the main cutout. Like the idea of .com to be separate or smaller and possible color. Looking for unique CalderW font design and a surrounding design per the examples below. Calder and G need to be different and the G a specific designing the mesh like the attached with the V in the mesh. But card side ways.. so mesh on right side of card with a G and .com in lower corner or where it fits
Also looking to add my main info on the back side of the card.
Derek M.
Cell
Email@mailbox-example.net

We are an commercial insurance broker specializing in program business.

Logo Text

CalderW.com

Font styles to use
Decorative
Script
Other font styles liked:

Requirements
Must have
• Must have Calder and G distinctively different
Nice to have
• On flat parts I want texture on top of card

```html
<!DOCTYPE html>
<html lang="en">
<head>
<meta charset="utf-8">
<title>CalderW Metal Business Card</title>
<link href="https://fonts.googleapis.com/css2?family=EB+Garamond:wght@400;500&display=swap" rel="stylesheet">
<style>
  :root {
    --page-bg: #e6e8ea;
    --card-black: #1c1c1c;
    --card-edge: #141414;
    --mesh-light: #f2f2f2;
    --mesh-mid: #9a9a9a;
    --mesh-dark: #5c554e;
    --silver: #c8c8c8;
    --accent-cyan: #1fa9d6;
  }
  * { margin: 0; padding: 0; box-sizing: border-box; }
  html, body {
    width: 1200px;
    height: 985px;
    overflow: hidden;
    background: var(--page-bg);
    font-family: "EB Garamond", Garamond, serif;
  }
  .canvas {
    position: relative;
    width: 1200px;
    height: 985px;
  }
  .card {
    position: absolute;
    left: 250px;
    width: 700px;
    height: 400px;
    border-radius: 26px;
    background: var(--card-black);
    border: 8px solid var(--card-edge);
    overflow: hidden;
  }
  .card--front { top: 70px; }
  .card--back { top: 515px; }

  .mesh-cutout {
    position: absolute;
    top: 0;
    bottom: 0;
    width: 250px;
  }
  .card--front .mesh-cutout {
    right: 0;
    background: linear-gradient(160deg, var(--mesh-light) 0%, #d8d8d8 60%, var(--mesh-mid) 100%);
  }
  .card--back .mesh-cutout {
    left: 0;
    background: linear-gradient(200deg, #cfcfcf 0%, var(--mesh-mid) 45%, var(--mesh-dark) 100%);
  }

  .brand-word,
  .brand-initial,
  .brand-domain {
    position: absolute;
    color: var(--silver);
    font-weight: 400;
    line-height: 1;
    white-space: nowrap;
  }
  .brand-word { letter-spacing: 0.06em; }

  .card--front .brand-word { left: 130px; top: 150px; font-size: 68px; }
  .card--front .brand-initial { left: 415px; top: 100px; font-size: 130px; }
  .card--front .brand-domain { left: 548px; top: 188px; font-size: 22px; }

  .card--back .brand-initial { left: 150px; top: 138px; font-size: 110px; }
  .card--back .brand-word { left: 292px; top: 180px; font-size: 56px; }
  .card--back .brand-domain { left: 160px; top: 250px; font-size: 20px; }

  .holder-name {
    position: absolute;
    left: 390px;
    top: 62px;
    color: var(--accent-cyan);
    font-size: 36px;
    font-weight: 500;
  }
  .contact {
    position: absolute;
    right: 40px;
    bottom: 28px;
    text-align: right;
    color: var(--accent-cyan);
    font-size: 22px;
    line-height: 1.45;
  }
</style>
</head>
<body>
<main class="canvas">

  <section class="card card--front" aria-label="Card front">
    <div class="mesh-cutout" role="img" aria-label="Cut-out geometric mesh panel in the metal, light showing through"></div>
    <div class="brand-word">Calder</div>
    <div class="brand-initial">W</div>
    <div class="brand-domain">.com</div>
  </section>

  <section class="card card--back" aria-label="Card back">
    <div class="mesh-cutout" role="img" aria-label="Cut-out geometric mesh panel in the metal, light showing through"></div>
    <div class="holder-name">Derek M.</div>
    <div class="brand-initial">W</div>
    <div class="brand-word">Calder</div>
    <div class="brand-domain">.com</div>
    <div class="contact">
      <p class="contact__phone">214.555.0178</p>
      <p class="contact__email">Derek@TeamCalderWorks.net</p>
    </div>
  </section>

</main>
</body>
</html>
```